6 Product labels for a Skincare brand

I have a logo and 6 label templates for 6 skincare productsI need someone to design the product labelsthe design of all 6 labels should be very similar just with basic adjustmentsPlease show me only the design for "Velaquin30ml_Template_V2" and then we can do the others

Target Market(s)

Women +45

Industry/Entity Type

Skin Care Product

Font styles to use
Other font styles liked:
• Helvetica

Colors
ffffff
fef7ee
feeeee
fbe7d2
fefced

Requirements
Must have
• Clean Clean design
• Company details are:
• Distributed by: MARLEE QUINTAV, Denver, CO 80000
• support@marleequintav.example, (866) 555-0172

```html
<!DOCTYPE html>
<html lang="en">
<head>
<meta charset="utf-8">
<title>Velaquin 30ml Label</title>
<link href="https://fonts.googleapis.com/css2?family=Source+Sans+3:ital,wght@0,400;0,600;0,700;1,400&display=swap" rel="stylesheet">
<style>
  :root {
    --sand: #f2dfc6;
    --blush: #fdeeee;
    --white: #ffffff;
    --ink: #231f20;
    --rule: #f2dfc6;
  }
  * { margin: 0; padding: 0; box-sizing: border-box; }
  html, body { width: 1200px; height: 999px; overflow: hidden; background: var(--white); }
  body { position: relative; font-family: "Source Sans 3", Helvetica, Arial, sans-serif; color: var(--ink); }

  .top-band { position: absolute; left: 120px; top: 54px; width: 961px; height: 27px; background: var(--sand); }

  .brand-name {
    position: absolute; left: 0; width: 1200px; text-align: center;
    font-family: "Source Sans 3", Helvetica, Arial, sans-serif; font-weight: 600;
    color: var(--ink); line-height: 1.2; text-transform: uppercase;
  }
  .brand-name--large { top: 142px; font-size: 32px; letter-spacing: 9px; padding-left: 9px; }

  .front-panel { position: absolute; left: 163px; top: 290px; width: 870px; height: 270px; background: var(--sand); }
  .front-panel .blush-strip { position: absolute; left: 0; top: 0; width: 100%; height: 53px; background: var(--blush); }
  .front-panel .gap-line { position: absolute; left: 0; top: 53px; width: 100%; height: 5px; background: var(--white); }
  .front-panel .name-plate { position: absolute; left: 214px; top: 15px; }
  .product-name {
    position: absolute; left: 0; width: 870px; top: 16px; text-align: center;
    font-weight: 600; font-size: 58px; line-height: 72px; color: var(--ink);
  }
  .volume { position: absolute; left: 0; width: 870px; top: 212px; text-align: center; font-size: 32px; line-height: 40px; }

  .fold-rule { position: absolute; left: 18px; top: 619px; width: 1165px; height: 5px; background: var(--rule); }

  .info-block { position: absolute; left: 31px; top: 637px; width: 295px; font-size: 10px; line-height: 12px; }
  .info-block p { margin-bottom: 6px; }
  .info-block strong { font-weight: 700; }
  .distributor { position: absolute; left: 31px; top: 716px; width: 222px; font-size: 9.4px; line-height: 12px; white-space: nowrap; }
  .distributor strong { font-weight: 700; }
  .distributor em { font-style: italic; }
  .version-tag { position: absolute; left: 260px; top: 707px; font-size: 8px; line-height: 10px; }
  .version-box { position: absolute; left: 260px; top: 720px; width: 53px; height: 17px; border: 1px solid var(--ink); }

  .brand-name--small { top: 637px; left: 505px; width: 100px; font-size: 8px; letter-spacing: 2.2px; padding-left: 2px; line-height: 11px; }

  .mini-panel { position: absolute; left: 449px; top: 676px; width: 213px; height: 65px; background: var(--sand); }
  .mini-panel .blush-strip { position: absolute; left: 0; top: 0; width: 100%; height: 12px; background: var(--blush); }
  .mini-panel .gap-line { position: absolute; left: 0; top: 12px; width: 100%; height: 2px; background: var(--white); }
  .mini-panel .name-plate { position: absolute; left: 52px; top: 3px; }
  .mini-panel .product-name { width: 213px; top: 3px; font-size: 13px; line-height: 20px; }
  .mini-panel .volume { width: 213px; top: 51px; font-size: 8px; line-height: 10px; }

  .ingredients {
    position: absolute; left: 753px; top: 637px; width: 420px;
    font-size: 8px; line-height: 10px; text-align: justify;
  }
  .ingredients strong { font-weight: 700; }
  .organic-note { position: absolute; right: 27px; top: 722px; font-size: 8px; }
</style>
</head>
<body>
  <div class="top-band"></div>

  <div class="brand-name brand-name--large">Marlee<br>Quintav</div>

  <section class="front-panel">
    <div class="blush-strip"></div>
    <div class="gap-line"></div>
    <svg class="name-plate" width="443" height="81" viewBox="0 0 443 81">
      <polygon points="22,0 421,0 443,40 421,81 22,81 0,40" fill="var(--white)"/>
    </svg>
    <div class="product-name">Velaquin</div>
    <div class="volume">30 ml | 1 fl oz</div>
  </section>

  <div class="fold-rule"></div>

  <div class="info-block">
    <p><strong>DIRECTIONS:</strong> Apply evenly over the face and neck. Use twice daily as part of your anti-aging regime or as needed for added moisture.</p>
    <p><strong>CAUTION:</strong> For external use only. Avoid direct contact with eyes. If irritation occurs, discontinue use.</p>
  </div>
  <div class="distributor">
    <strong>Distributed By</strong>: MARLEE QUINTAV, Denver, CO 80000<br>
    <em>support@marleequintav.example, (866) 555-0172</em>
  </div>
  <div class="version-tag">T-V2</div>
  <div class="version-box"></div>

  <div class="brand-name brand-name--small">Marlee<br>Quintav</div>

  <section class="mini-panel">
    <div class="blush-strip"></div>
    <div class="gap-line"></div>
    <svg class="name-plate" width="108" height="20" viewBox="0 0 108 20">
      <polygon points="6,0 102,0 108,10 102,20 6,20 0,10" fill="var(--white)"/>
    </svg>
    <div class="product-name">Velaquin</div>
    <div class="volume">30 ml | 1 fl oz</div>
  </section>

  <div class="ingredients">
    <strong>INGREDIENTS:</strong> Water, Prunus Amygdalus Dulcis (Sweet Almond) Oil, Caprylic/Capric Triglyceride, Myristic Acid, Stearic Acid, Cetyl Esters, Glyceryl Stearate SE, Aloe Barbadensis (Aloe Vera) Leaf Juice*, Cetearyl Alcohol, Ceteareth-20, Diheptyl Succinate, Capryloyl Glycerin/Sebacic Acid Copolymer, Pyrus Malus (Apple) Fruit Extract, Glycerin, Dehydroacetic Acid, Benzyl Alcohol, Saccharide Isomerate, Acetyl Hexapeptide-30, Arginine, Caprylyl Glycol, Tromethamine, Carbomer, Potassium Sorbate, Squalane, Tocopheryl Acetate, Ubiquinone, Fagus Sylvatica Bud Extract, Sodium Carboxymethyl Beta-Glucan, Taraxacum Ocinale (Dandelion) Leaf Extract, Salvia Ocinalis (Sage) Leaf Extract, Melissa Ocinalis Leaf Extract, Sodium Benzoate, Citric Acid
  </div>
  <div class="organic-note">*Certified Organic Ingredients</div>
</body>
</html>
```